Artist/Artwork Product Catalog

I need a small brief product catalog to display my art for purchase to my interior designer clients, to purchase for their clients. Should be 5 - 10 pages with art/canvas display mock up pictures. Sections should include About the artist, space for pricing and art titles, Editable Section Names (3 sections-not including previously mentioned sections), Contact info-including social media. I would like modern and simplistic. My art is filled with bright colors and as such want the design of the catalog to be black and white so as not to detract from the art itself. Please refer to my website and instagram for further design resource: www.torevandrelle.com ; @vandrelletor (instagram)
Target Market(s)
Interior Designers, Collectors, Galleries
Industry/Entity Type
Art Gallery
Font styles to use
Colors
Designer to choose colors to be used in the design.
Requirements
Must have
- Must have my artwork included in catalog displayed in canvas wall art mock up. Will send files upon acceptance of catalog design. Need to be printer ready upon project completion as well as editable for future changes as needed. Would like a smaller sized catalog, maybe A4.
Nice to have
- Editable for future use. Would love to have new logo integrated into catalog.
Should not have
- No distracting colors or ornate decorative design

```html
<!DOCTYPE html>
<html lang="en">
<head>
<meta charset="utf-8">
<title>TOR Product Catalog – Cover</title>
<link rel="stylesheet" href="https://fonts.googleapis.com/css2?family=Montserrat:wght@200;400;600&display=swap">
<style>
  :root {
    --backdrop: #e6e6e4;
    --paper: #f1f1ef;
    --paper-shade: #e3e3e0;
    --ink: #3a3a3a;
    --ink-soft: #4a4a4a;
    --label: #2f2f2f;
    --white: #ffffff;
  }
  * { margin: 0; padding: 0; box-sizing: border-box; }
  html, body { width: 1200px; height: 699px; overflow: hidden; }
  body {
    background: var(--backdrop);
    font-family: "Montserrat", sans-serif;
    position: relative;
  }
  .side-label {
    position: absolute;
    font-weight: 200;
    font-size: 46px;
    line-height: 1;
    letter-spacing: 2px;
    color: var(--label);
    white-space: nowrap;
  }
  .side-label--front { left: 190px; top: 90px; }
  .side-label--back {
    left: 812px; top: 660px;
    transform: rotate(-90deg);
    transform-origin: left top;
  }

  .cover-front {
    position: absolute;
    left: 200px; top: 150px;
    width: 580px; height: 430px;
    background: var(--paper);
    overflow: hidden;
    box-shadow: 0 6px 18px rgba(0,0,0,0.12);
  }
  .cover-front__motif {
    position: absolute;
    left: -70px; top: 40px;
    width: 430px; height: 430px;
    border-radius: 50%;
    background: var(--paper-shade);
  }
  .brand-band {
    position: absolute;
    left: 0; top: 115px;
    width: 290px; height: 90px;
    background: var(--ink);
    display: flex; align-items: center;
    padding-left: 42px; gap: 18px;
  }
  .brand-band__mark {
    width: 26px; height: 26px;
    background: var(--white);
  }
  .brand-band__name {
    color: var(--white);
    font-weight: 600;
    font-size: 32px;
    letter-spacing: 12px;
  }
  .cover-front__title {
    position: absolute;
    right: 70px; bottom: 62px;
    font-weight: 400;
    font-size: 28px;
    line-height: 1;
    letter-spacing: 3px;
    color: var(--ink-soft);
    white-space: nowrap;
  }
  .cover-front__rule {
    position: absolute;
    right: 44px; bottom: 62px;
    width: 3px; height: 62px;
    background: var(--ink);
  }

  .cover-back {
    position: absolute;
    left: 900px; top: 480px;
    width: 240px; height: 160px;
    background: var(--ink);
    display: flex; align-items: center; justify-content: center;
    box-shadow: 0 5px 14px rgba(0,0,0,0.18);
  }
  .cover-back__mark {
    width: 20px; height: 20px;
    background: var(--white);
  }
</style>
</head>
<body>
  <div class="side-label side-label--front">FRONT</div>

  <section class="cover-front" aria-label="Front cover">
    <div class="cover-front__motif"></div>
    <div class="brand-band">
      <span class="brand-band__mark"></span>
      <span class="brand-band__name">TOR</span>
    </div>
    <h1 class="cover-front__title">PRODUCT CATALOG</h1>
    <span class="cover-front__rule"></span>
  </section>

  <div class="side-label side-label--back">BACK</div>

  <section class="cover-back" aria-label="Back cover">
    <span class="cover-back__mark"></span>
  </section>
</body>
</html>
```